QBrook718 Business Card Design

I am in need of a business card design.

Business Name: Harbor Stone 718 or QBrook718 (we can try the business card with both variations)

I would like it to be somewhat different from the "average" business card

What do we do?

We link up with distributors of different items and we Market their products, sell their products, fulfill the shipment, and handle all customer service that goes along with it.

I will be uploading our logo as well as other business card ideas that i have seen and liked on the web.

I like the style of the "graphic design" business card that i uploaded. I was thinking maybe something like that but instead would read.

SYNC | SELL | SHIP

With maybe:
a computer or a Sync icon underneath SYNC
Some form of money sign underneath Sell
a delivery truck or something underneath SHIP.

And then I was thinking maybe put the logo on the back side like in the other business card that i uploaded.

I definitely want a double sided business card.

These are only my suggestions and if i was very confident in my idea then I wouldn't have to be on here. (So make what you think is nice because my opinion is probably not so great anyway!!)

Everything can be changed.

ALSO, For the logo
We can try and remove the text multi channel selling

For the Business card contact info:
Tom Haskins
CEO
2419 Pelkey Avenue
J7R-2B8
Montreal, Quebec

Thanks

Target Market(s)

Businesses

Industry/Entity Type

Information Technology

Font styles to use
Serif
Sans Serif
Decorative

Colors
34a6d6
33b8a4
aaaaaa
85cae6
33a6d7
0492cd
9d9d9d

Requirements
Must have
• Double Sided Business card
Nice to have
• Illustration graphics / Icons underneath the main points

```html
<!DOCTYPE html>
<html lang="en">
<head>
<meta charset="utf-8">
<title>QBrook718 Business Card</title>
<link href="https://fonts.googleapis.com/css2?family=Questrial&display=swap" rel="stylesheet">
<style>
  :root {
    --stage: #e6e6e4;
    --card-dark: #2b2b2d;
    --card-blue: #2aa7e0;
    --brand-blue: #1e9bd7;
    --accent-green: #7cc243;
    --text-light: #e9e9e9;
    --text-muted: #b9b9b9;
    --ink-grey: #5d5f62;
    --white: #ffffff;
  }
  * { margin: 0; padding: 0; box-sizing: border-box; }
  html, body { width: 1200px; height: 1021px; overflow: hidden; }
  body {
    background: var(--stage);
    font-family: "Questrial", sans-serif;
    display: flex;
    flex-direction: column;
    align-items: center;
    justify-content: center;
    gap: 56px;
  }
  .card {
    width: 770px;
    height: 440px;
    position: relative;
    box-shadow: 0 10px 28px rgba(0,0,0,0.18);
  }
  .card--front { background: var(--card-dark); }
  .card--back { background: var(--card-blue); }

  /* front */
  .front-brand {
    position: absolute;
    left: 90px;
    top: 175px;
    display: flex;
    align-items: center;
    gap: 16px;
  }
  .brand-dot {
    width: 34px; height: 34px; border-radius: 50%;
    background: var(--accent-green);
  }
  .brand-name {
    font-size: 52px;
    color: var(--brand-blue);
    letter-spacing: 0.5px;
  }
  .front-tagline {
    position: absolute;
    left: 142px;
    top: 246px;
    font-size: 17px;
    color: var(--text-light);
    letter-spacing: 1px;
  }
  .contact {
    position: absolute;
    left: 470px;
    top: 118px;
    color: var(--text-muted);
  }
  .contact-name { font-size: 30px; color: var(--text-light); }
  .contact-role { font-size: 17px; color: var(--brand-blue); margin: 4px 0 14px; }
  .contact-row {
    display: flex;
    gap: 12px;
    font-size: 15px;
    line-height: 1.55;
    margin-bottom: 6px;
  }
  .contact-row svg { flex: none; margin-top: 4px; }

  /* back */
  .back-brand {
    position: absolute;
    left: 0; right: 0;
    top: 100px;
    display: flex;
    justify-content: center;
    align-items: center;
    gap: 16px;
  }
  .back-brand .brand-name { color: var(--white); font-size: 60px; }
  .pillars {
    position: absolute;
    left: 0; right: 0;
    top: 235px;
    display: flex;
    justify-content: center;
    align-items: flex-end;
    gap: 26px;
  }
  .pillar {
    display: flex;
    flex-direction: column;
    align-items: center;
    gap: 14px;
    width: 130px;
  }
  .pillar-label {
    font-size: 30px;
    color: var(--white);
    letter-spacing: 2px;
  }
  .divider {
    width: 2px;
    height: 34px;
    background: var(--white);
    margin-bottom: 4px;
  }
</style>
</head>
<body>

<section class="card card--front" aria-label="Business card front">
  <div class="front-brand">
    <span class="brand-dot"></span>
    <span class="brand-name">QBrook718</span>
  </div>
  <p class="front-tagline">Multi Channel Selling</p>

  <div class="contact">
    <p class="contact-name">Tom Haskins</p>
    <p class="contact-role">CEO</p>
    <div class="contact-row">
      <svg width="14" height="18" viewBox="0 0 14 18"><path d="M7 0a7 7 0 0 0-7 7c0 5 7 11 7 11s7-6 7-11a7 7 0 0 0-7-7z" fill="var(--accent-green)"/><circle cx="7" cy="7" r="2.5" fill="var(--card-dark)"/></svg>
      <span>2419 Pelkey Avenue<br>J7R-2B8<br>Montreal, Quebec</span>
    </div>
    <div class="contact-row">
      <svg width="16" height="14" viewBox="0 0 16 14"><path d="M1 4c0-2 3-3 7-3s7 1 7 3v1h-4V4H5v1H1z M3 7h10l1 6H2z" fill="var(--accent-green)"/><circle cx="8" cy="10" r="1.6" fill="var(--card-dark)"/></svg>
      <span>000 000 0000</span>
    </div>
    <div class="contact-row">
      <svg width="16" height="12" viewBox="0 0 16 12"><rect width="16" height="12" fill="var(--accent-green)"/><path d="M0 0l8 6 8-6" stroke="var(--card-dark)" stroke-width="1.4" fill="none"/></svg>
      <span>hello@qbrook718.ca</span>
    </div>
  </div>
</section>

<section class="card card--back" aria-label="Business card back">
  <div class="back-brand">
    <span class="brand-dot"></span>
    <span class="brand-name">QBrook718</span>
  </div>

  <div class="pillars">
    <div class="pillar">
      <svg class="pillar-icon" width="58" height="52" viewBox="0 0 58 52" aria-hidden="true">
        <rect x="2" y="2" width="54" height="36" rx="2" fill="none" stroke="var(--ink-grey)" stroke-width="3"/>
        <rect x="10" y="12" width="22" height="3" fill="var(--ink-grey)"/>
        <rect x="10" y="19" width="18" height="3" fill="var(--ink-grey)"/>
        <rect x="10" y="26" width="22" height="3" fill="var(--ink-grey)"/>
        <path d="M40 10a8 8 0 1 0 8 8h-8z" fill="var(--ink-grey)"/>
        <rect x="26" y="38" width="6" height="8" fill="var(--ink-grey)"/>
        <rect x="16" y="46" width="26" height="3" fill="var(--ink-grey)"/>
      </svg>
      <span class="pillar-label">SYNC</span>
    </div>
    <span class="divider"></span>
    <div class="pillar">
      <svg class="pillar-icon" width="52" height="52" viewBox="0 0 52 52" aria-hidden="true">
        <circle cx="26" cy="26" r="23" fill="none" stroke="var(--ink-grey)" stroke-width="3"/>
        <text x="26" y="35" text-anchor="middle" font-family="Questrial, sans-serif" font-size="28" fill="var(--ink-grey)">$</text>
      </svg>
      <span class="pillar-label">SELL</span>
    </div>
    <span class="divider"></span>
    <div class="pillar">
      <svg class="pillar-icon" width="52" height="52" viewBox="0 0 52 52" aria-hidden="true">
        <circle cx="26" cy="26" r="25" fill="var(--ink-grey)"/>
        <rect x="10" y="18" width="20" height="13" fill="var(--card-blue)"/>
        <path d="M30 22h7l5 5v4H30z" fill="var(--card-blue)"/>
        <circle cx="16" cy="33" r="3" fill="var(--card-blue)"/>
        <circle cx="36" cy="33" r="3" fill="var(--card-blue)"/>
      </svg>
      <span class="pillar-label">SHIP</span>
    </div>
  </div>
</section>

</body>
</html>
```